Corvale Real Estate

I manage 2 firms. The first one is Felmont and the logo is in blue (see the file) but i need a design for my business card for the second firm called CORVALE IMMOBILIER. This one is in charge of Real estate developer.

Colors
3176b5

```html
<!DOCTYPE html>
<html lang="en">
<head>
<meta charset="utf-8">
<title>Corvale Immobilier – Business Card</title>
<link href="https://fonts.googleapis.com/css2?family=Montserrat:wght@600;700&family=Poppins:wght@500;600&display=swap" rel="stylesheet">
<style>
  :root {
    --navy: #262b6a;
    --orange: #f05a28;
    --paper: #ffffff;
    --backdrop: #d1d2d4;
    --rule: #e3e4e8;
  }
  * { margin: 0; padding: 0; box-sizing: border-box; }
  html, body { width: 1200px; height: 1200px; overflow: hidden; }
  body { background: var(--backdrop); position: relative; font-family: "Poppins", sans-serif; color: var(--navy); }

  .card { position: absolute; left: 320px; width: 561px; height: 321px; background: var(--paper); overflow: hidden; }
  .card--front { top: 185px; }
  .card--back { top: 625px; }

  .band { position: absolute; width: 280px; height: 38px; }
  .band--top { left: 0; top: 0; background: var(--navy); border-bottom-right-radius: 30px; }
  .band--bottom { right: 0; bottom: 0; background: var(--orange); border-top-left-radius: 30px; }

  .brand { position: absolute; display: flex; align-items: center; font-family: "Montserrat", sans-serif; font-weight: 700; color: var(--navy); }
  .brand__mark { background: var(--navy); flex: none; }
  .brand__name { display: flex; flex-direction: column; line-height: 1; }

  .card--front .brand { left: 95px; top: 140px; gap: 20px; }
  .card--front .brand__mark { width: 78px; height: 78px; }
  .card--front .brand__line1 { font-size: 54px; letter-spacing: 1px; }
  .card--front .brand__line2 { font-size: 27px; letter-spacing: 9.5px; margin-top: 6px; }

  .card--back .brand { left: 154px; top: 42px; gap: 14px; }
  .card--back .brand__mark { width: 58px; height: 58px; }
  .card--back .brand__line1 { font-size: 38px; letter-spacing: 0.5px; }
  .card--back .brand__line2 { font-size: 18.5px; letter-spacing: 6.5px; margin-top: 4px; }

  .tab { position: absolute; top: 111px; width: 17px; height: 100px; }
  .tab--left { left: 0; background: var(--orange); border-radius: 0 6px 6px 0; }
  .tab--right { right: 0; background: var(--navy); border-radius: 6px 0 0 6px; }

  .divider { position: absolute; left: 150px; width: 261px; height: 2px; background: linear-gradient(90deg, transparent, var(--rule) 30%, var(--rule) 70%, transparent); }
  .divider--top { top: 133px; }
  .divider--bottom { top: 201px; }

  .person { position: absolute; left: 0; width: 100%; text-align: center; }
  .person__name { top: 154px; font-family: "Montserrat", sans-serif; font-weight: 700; font-size: 18px; letter-spacing: 5px; }
  .person__role { top: 180px; font-family: "Montserrat", sans-serif; font-weight: 600; font-size: 11.5px; letter-spacing: 3.6px; }

  .contacts { position: absolute; left: 166px; top: 206px; list-style: none; }
  .contacts li { display: flex; align-items: center; gap: 10px; height: 19.5px; font-size: 11.5px; font-weight: 600; }
  .contacts svg { width: 15px; height: 15px; fill: var(--navy); flex: none; }
</style>
</head>
<body>
  <section class="card card--front">
    <div class="band band--top"></div>
    <div class="brand">
      <span class="brand__mark"></span>
      <span class="brand__name">
        <span class="brand__line1">CORVALE</span>
        <span class="brand__line2">IMMOBILIER</span>
      </span>
    </div>
    <div class="band band--bottom"></div>
  </section>

  <section class="card card--back">
    <div class="brand">
      <span class="brand__mark"></span>
      <span class="brand__name">
        <span class="brand__line1">CORVALE</span>
        <span class="brand__line2">IMMOBILIER</span>
      </span>
    </div>
    <div class="tab tab--left"></div>
    <div class="tab tab--right"></div>
    <div class="divider divider--top"></div>
    <p class="person person__name">YOUR NAME HERE</p>
    <p class="person person__role">YOUR DESIGNATION HERE</p>
    <div class="divider divider--bottom"></div>
    <ul class="contacts">
      <li>
        <svg viewBox="0 0 24 24"><path d="M6.6 10.8a15.1 15.1 0 0 0 6.6 6.6l2.2-2.2a1 1 0 0 1 1-.25 11.4 11.4 0 0 0 3.6.57 1 1 0 0 1 1 1V20a1 1 0 0 1-1 1A17 17 0 0 1 3 4a1 1 0 0 1 1-1h3.5a1 1 0 0 1 1 1c0 1.25.2 2.45.57 3.57a1 1 0 0 1-.25 1z"/></svg>
        <span>+33 1 40 22 17 85</span>
      </li>
      <li>
        <svg viewBox="0 0 24 24"><path d="M2 5h20v14H2zm2 2v.5l8 5.5 8-5.5V7zm0 3v7h16v-7l-8 5.5z"/></svg>
        <span>your e-mail address here</span>
      </li>
      <li>
        <svg viewBox="0 0 24 24"><path d="M12 2a10 10 0 1 0 0 20 10 10 0 0 0 0-20zm0 2a8 8 0 0 1 7.7 6h-3.2a14 14 0 0 0-1.6-5.5A8 8 0 0 1 12 4zm-3 .5A14 14 0 0 0 7.5 10H4.3A8 8 0 0 1 9 4.5zM4.3 14h3.2A14 14 0 0 0 9 19.5 8 8 0 0 1 4.3 14zm5.2 0h5a12 12 0 0 1-2.5 5.7A12 12 0 0 1 9.5 14zm0-4A12 12 0 0 1 12 4.3 12 12 0 0 1 14.5 10zm5.4 9.5a14 14 0 0 0 1.6-5.5h3.2a8 8 0 0 1-4.8 5.5z"/></svg>
        <span>www.corvale-immo.fr</span>
      </li>
      <li>
        <svg viewBox="0 0 24 24"><path d="M12 2a7 7 0 0 0-7 7c0 5.2 7 13 7 13s7-7.8 7-13a7 7 0 0 0-7-7zm0 9.5A2.5 2.5 0 1 1 12 6.5a2.5 2.5 0 0 1 0 5z"/></svg>
        <span>14 Rue Valmont, 75116 Paris, France</span>
      </li>
    </ul>
  </section>
</body>
</html>
```